Flyer to Promote Membership in a Trade Association

UPDATE: I am looking for something modern and clean. NO CLIP ART. Not flashy. Just professional and modern. For everyone looking at our current flyer, we don't like it. That's why we aer looking for a new one. So please don't replicate it or use it as inspiration.

I need a flyer to promote membership in the Durable Residence Backers League. It can (probably should) be 2-sided. The content is attached as well as our logo and brand guidelines.

```html
<!DOCTYPE html>
<html lang="en">
<head>
<meta charset="utf-8">
<title>Join DRBL Today</title>
<link rel="stylesheet" href="https://fonts.googleapis.com/css2?family=Noto+Serif:wght@300;400;700&display=swap">
<style>
  :root {
    --orange: #F47F30;
    --orange-deep: #DD6628;
    --orange-mid: #E9722E;
    --charcoal: #414142;
    --charcoal-shade: #3B3B3C;
    --white: #FFFFFF;
  }
  * { box-sizing: border-box; margin: 0; padding: 0; }
  html, body { width: 849px; height: 1200px; overflow: hidden; }
  body {
    position: relative;
    background: var(--orange);
    color: var(--white);
    font-family: "Noto Serif", Georgia, serif;
    font-weight: 300;
  }
  .intro {
    position: absolute; left: 59px; top: 58px; width: 790px;
    font-size: 29px; line-height: 36px; font-weight: 300; letter-spacing: -0.4px;
  }
  .join-title {
    position: absolute; left: 59px; top: 148px;
    font-size: 34px; font-weight: 700; line-height: 44px;
  }
  .tier {
    position: absolute; top: 226px; width: 349px; height: 156px;
    border-radius: 9px; text-align: center;
    display: flex; flex-direction: column; justify-content: center;
    font-size: 16px; line-height: 20.5px;
  }
  .tier--investor { left: 59px; background: var(--orange-deep); }
  .tier--affiliate { left: 442px; background: var(--orange-mid); }
  .tier-name { font-size: 20px; font-weight: 700; line-height: 24px; }
  .tier-price { font-weight: 700; }
  .benefits-heading {
    position: absolute; top: 402px; left: 0; width: 849px;
    display: flex; justify-content: center; align-items: center; gap: 38px;
    font-size: 34px; font-weight: 700; line-height: 46px;
  }
  .benefits-heading .rule { width: 48px; height: 1.5px; background: var(--white); }
  .benefits-heading .rule--right { width: 54px; }
  .benefits {
    position: absolute; top: 469px; left: 34px; width: 781px;
    text-align: center; list-style: none;
  }
  .benefit { margin-bottom: 12px; }
  .benefit-title { font-size: 16px; font-weight: 700; line-height: 20px; }
  .benefit-text { font-size: 16px; line-height: 20.5px; }
  .tag { margin-left: 8px; }
  .members {
    position: absolute; top: 972px; left: 0; width: 849px; height: 228px;
    background: var(--charcoal); overflow: hidden;
  }
  .members-shapes { position: absolute; inset: 0; }
  .members-content { position: relative; text-align: center; }
  .members-title {
    padding-top: 26px; font-size: 12.5px; font-weight: 700; line-height: 16px;
  }
  .members-list {
    width: 780px; margin: 0 auto; font-size: 12.5px; line-height: 15.5px; font-weight: 300;
  }
  .cta-title {
    margin-top: 28px; font-size: 34px; font-weight: 700; line-height: 40px;
  }
  .cta-url {
    font-size: 16px; font-weight: 700; line-height: 20px; color: var(--orange);
  }
</style>
</head>
<body>
  <p class="intro">One membership, unlimited access. Your entire team can participate in DRBL activities.</p>
  <h1 class="join-title">Join DRBL Today</h1>

  <section class="tier tier--investor">
    <h2 class="tier-name">Investor Members</h2>
    <p>Banks, Insurance Companies,<br>Economic Investors</p>
    <p class="tier-price">$5,000/year (assets ≥$5B)<br>$1,000/year (assets &lt;$5B)</p>
  </section>
  <section class="tier tier--affiliate">
    <h2 class="tier-name">Affiliate Members</h2>
    <p>Syndicators &amp; Brokers</p>
    <p class="tier-price">$4,500/year</p>
  </section>

  <h2 class="benefits-heading"><span class="rule"></span>Member Benefits<span class="rule rule--right"></span></h2>

  <ul class="benefits">
    <li class="benefit">
      <h3 class="benefit-title">Members-Only Conferences</h3>
      <p class="benefit-text">Two annual in-person meetings. Spring Meeting: investors-only for candid peer conversations. Fall Summit: full ecosystem gathering with syndicators and brokers.</p>
    </li>
    <li class="benefit">
      <h3 class="benefit-title">Investor-Only Forums</h3>
      <p class="benefit-text">Exclusive meetings and webinars for investors only, enabling candid conversations and meaningful collaboration.</p>
    </li>
    <li class="benefit">
      <h3 class="benefit-title">Peer-to-Peer Meetups</h3>
      <p class="benefit-text">Find your peers—underwriters, asset managers, credit officers and more—with our meetups.</p>
    </li>
    <li class="benefit">
      <h3 class="benefit-title">Live &amp; On-Demand Webinars</h3>
      <p class="benefit-text">Free monthly Third Thursday webinars covering Year 15 issues, secondary transactions, securitizing developer fees and other emerging topics.</p>
    </li>
    <li class="benefit">
      <h3 class="benefit-title">Searchable Member Directory</h3>
      <p class="benefit-text">Find underwriters, asset managers, and credit officers—searchable by role,<br>firm type, and investment approach.</p>
    </li>
    <li class="benefit">
      <h3 class="benefit-title">Shape Industry Standards<span class="tag">[INVESTOR ONLY]</span></h3>
      <p class="benefit-text">DRBL's underwriting and asset management standards are adopted industry-wide.<br>Influence them through our committees.</p>
    </li>
    <li class="benefit">
      <h3 class="benefit-title">Emerging Leaders Program<span class="tag">[INVESTOR ONLY]</span></h3>
      <p class="benefit-text">Develop your firm's next-generation leaders through dedicated professional<br>development programming.</p>
    </li>
  </ul>

  <footer class="members">
    <svg class="members-shapes" width="849" height="228" viewBox="0 0 849 228" aria-hidden="true">
      <polygon points="107,228 107,120 280,20 445,100 445,228" fill="var(--charcoal-shade)"/>
      <polygon points="445,0 620,0 700,228 445,228" fill="var(--charcoal-shade)" opacity="0.6"/>
    </svg>
    <div class="members-content">
      <h2 class="members-title">Our Investor Members Include</h2>
      <p class="members-list">Halvern Life/Corbel Health • Brightwater Bank • Pinecrest National Bank • Bank of Elmsford • Tarrow Hale Bank • Quillon Financial • Norvale One • Ashcombe Trust Bank • NVRB • Sixth Meridian CDC • First Lantern Bank • Calloway Reese • Bellhaven Bank • Dunmore Pike • Larkspur Insurance • Westerly Life • Orison (FRTA) • Kelby Real Estate • Fairmount Affordable Housing • Redcliff Bank • Ormond Vance • QL Bank • Fernlea Bank • Stillwater Community Capital • Crestline Bank USA • MVSA • Granite Ridge Impact Finance • Harrowgate Bank</p>
      <p class="cta-title">Ready to join?</p>
      <p class="cta-url">drbl-league.org</p>
    </div>
  </footer>
</body>
</html>
```